Powerpoint Presentation

We have a basic 8 page presentation that we would like created on powerpoint. The presentation is very simple dot points and we would like to jazz it up with relevant photos/images relating to the topic on each page.

The topic of the presentation is 'creating a powerful presence and knowing your personal brand' (see attached files).

Target Market(s)

Business women

Requirements
Must have
• Images that match the content on each page

```html
<!DOCTYPE html>
<html lang="en">
<head>
<meta charset="utf-8">
<title>Elevator Pitch</title>
<link rel="stylesheet" href="https://fonts.googleapis.com/css2?family=Open+Sans:wght@400;700&display=swap">
<style>
  :root {
    --sky-top: #1a9be8;
    --sky-mid: #49b6f2;
    --sky-light: #9fd9fa;
    --wave-pale: #d6effc;
    --page: #ffffff;
    --ink: #17285e;
    --bullet: #3aa6e6;
    --figure-light: rgba(236, 214, 190, 0.95);
    --figure-mid: rgba(222, 196, 168, 0.55);
    --figure-fade: rgba(255, 255, 255, 0);
    --brand-accent: #e8622a;
    --brand-ink: #6b6b6b;
  }
  * { margin: 0; padding: 0; box-sizing: border-box; }
  html, body { width: 1200px; height: 900px; overflow: hidden; background: var(--page); }
  .slide {
    position: relative;
    width: 1200px;
    height: 900px;
    background: var(--page);
    font-family: "Open Sans", sans-serif;
    overflow: hidden;
  }
  .header-band { position: absolute; left: 0; top: 0; width: 1200px; height: 330px; }
  .slide-title {
    position: absolute;
    left: 0; top: 92px;
    width: 1200px;
    text-align: center;
    color: var(--page);
    font-weight: 700;
    font-size: 60px;
    line-height: 80px;
    letter-spacing: 0.5px;
  }
  .points {
    position: absolute;
    left: 126px; top: 310px;
    list-style: none;
    color: var(--ink);
    font-size: 53px;
    line-height: 88px;
  }
  .points li { position: relative; padding-left: 42px; }
  .points li::before {
    content: "*";
    position: absolute;
    left: 0; top: 4px;
    color: var(--bullet);
    font-size: 50px;
  }
  .points strong { font-weight: 700; }
  .figure-art {
    position: absolute;
    left: 560px; top: 505px;
    width: 380px; height: 380px;
    border-radius: 50%;
    background: radial-gradient(ellipse 50% 50% at 50% 50%, var(--figure-light) 0%, var(--figure-mid) 55%, var(--figure-fade) 100%);
  }
  .brand {
    position: absolute;
    left: 18px; bottom: 22px;
    display: flex;
    align-items: center;
    gap: 10px;
  }
  .brand-dot { width: 30px; height: 30px; border-radius: 50%; background: var(--brand-accent); }
  .brand-name { color: var(--brand-ink); font-size: 21px; font-weight: 400; }
</style>
</head>
<body>
<main class="slide">
  <svg class="header-band" viewBox="0 0 1200 330" aria-hidden="true">
    <defs>
      <linearGradient id="sky" x1="0" y1="0" x2="0" y2="1">
        <stop offset="0" stop-color="#1a9be8"/>
        <stop offset="0.6" stop-color="#49b6f2"/>
        <stop offset="1" stop-color="#9fd9fa"/>
      </linearGradient>
    </defs>
    <rect width="1200" height="330" fill="url(#sky)"/>
    <path d="M0 240 C 250 200, 520 180, 800 215 C 980 238, 1100 270, 1200 300 L1200 330 L0 330 Z" fill="#d6effc" opacity="0.7"/>
    <path d="M0 250 C 300 185, 620 175, 900 230 C 1020 254, 1120 290, 1200 315" fill="none" stroke="#ffffff" stroke-width="3" opacity="0.8"/>
    <path d="M560 300 C 800 250, 1000 215, 1200 205" fill="none" stroke="#ffffff" stroke-width="2" opacity="0.7"/>
    <path d="M0 255 C 220 210, 420 205, 620 235 C 760 256, 860 290, 960 330 L0 330 Z" fill="#ffffff"/>
    <path d="M0 262 C 400 232, 760 260, 1200 330 L0 330 Z" fill="#ffffff"/>
  </svg>

  <h1 class="slide-title">Elevator Pitch</h1>

  <ul class="points">
    <li>What do you do?</li>
    <li>What is <strong>your</strong> value proposition?</li>
  </ul>

  <div class="figure-art" role="img" aria-label="Illustration of a faceless figure with a question mark on its head, shrugging with open arms"></div>

  <div class="brand">
    <span class="brand-dot"></span>
    <span class="brand-name">open step studio</span>
  </div>
</main>
</body>
</html>
```